Step and Repeat Backdrop for wedding reception photo booth

Would like to have a Step and Repeat Backdrop (8 foot high by 10 foot wide) that incorporates the wedding logo (attached) and the names Elena and Gavin. Background should be white, and wedding colors are burgundy and gold. Show me creativity :-) I have included some random samples.

```html
<!DOCTYPE html>
<html lang="en">
<head>
<meta charset="utf-8">
<title>Elena &amp; Gavin – Step and Repeat Backdrop</title>
<link rel="stylesheet" href="https://fonts.googleapis.com/css2?family=Cormorant+Garamond:wght@500&display=swap">
<style>
  :root {
    --stage: #8c8c8c;
    --cream-top: #fdfaf2;
    --cream-mid: #f6ecd6;
    --cream-bottom: #e8d3a6;
    --gold: #a4834a;
  }
  * { margin: 0; padding: 0; box-sizing: border-box; }
  html, body {
    width: 768px;
    height: 1200px;
    overflow: hidden;
    background: var(--stage);
  }
  .canvas {
    width: 768px;
    height: 1200px;
    display: flex;
    align-items: center;
    justify-content: center;
  }
  .backdrop {
    position: relative;
    width: 700px;
    height: 560px;
    background: linear-gradient(180deg, var(--cream-top) 0%, var(--cream-mid) 55%, var(--cream-bottom) 100%);
    box-shadow: 0 2px 6px rgba(0,0,0,0.18);
    overflow: hidden;
  }
  .repeat-grid {
    position: absolute;
    inset: 14px 10px 14px 10px;
    display: grid;
    grid-template-columns: repeat(7, 1fr);
    grid-template-rows: repeat(8, 1fr);
    align-items: center;
    justify-items: center;
    list-style: none;
  }
  .repeat-mark {
    font-family: "Cormorant Garamond", Georgia, serif;
    font-weight: 500;
    font-size: 17px;
    color: var(--gold);
    letter-spacing: 0.5px;
    white-space: nowrap;
  }
  .repeat-mark--hidden { visibility: hidden; }
  .wedding-mark {
    position: absolute;
    left: 50%;
    top: 50%;
    transform: translate(-50%, -50%);
    display: flex;
    align-items: center;
    gap: 8px;
  }
  .bracket {
    width: 12px;
    height: 92px;
    flex: none;
  }
  .couple-names {
    font-family: "Cormorant Garamond", Georgia, serif;
    font-weight: 500;
    color: var(--gold);
    font-size: 50px;
    line-height: 0.95;
    letter-spacing: 0.5px;
  }
  .couple-names .first { display: block; }
  .couple-names .second { display: block; padding-left: 18px; }
</style>
</head>
<body>
  <main class="canvas">
    <section class="backdrop" aria-label="Step and repeat backdrop">
      <ul class="repeat-grid" aria-hidden="true">
        <li class="repeat-mark">E&amp;G</li><li class="repeat-mark">E&amp;G</li><li class="repeat-mark">E&amp;G</li><li class="repeat-mark">E&amp;G</li><li class="repeat-mark">E&amp;G</li><li class="repeat-mark">E&amp;G</li><li class="repeat-mark">E&amp;G</li>
        <li class="repeat-mark">E&amp;G</li><li class="repeat-mark">E&amp;G</li><li class="repeat-mark">E&amp;G</li><li class="repeat-mark">E&amp;G</li><li class="repeat-mark">E&amp;G</li><li class="repeat-mark">E&amp;G</li><li class="repeat-mark">E&amp;G</li>
        <li class="repeat-mark">E&amp;G</li><li class="repeat-mark">E&amp;G</li><li class="repeat-mark">E&amp;G</li><li class="repeat-mark">E&amp;G</li><li class="repeat-mark">E&amp;G</li><li class="repeat-mark">E&amp;G</li><li class="repeat-mark">E&amp;G</li>
        <li class="repeat-mark">E&amp;G</li><li class="repeat-mark">E&amp;G</li><li class="repeat-mark repeat-mark--hidden">E&amp;G</li><li class="repeat-mark repeat-mark--hidden">E&amp;G</li><li class="repeat-mark repeat-mark--hidden">E&amp;G</li><li class="repeat-mark">E&amp;G</li><li class="repeat-mark">E&amp;G</li>
        <li class="repeat-mark">E&amp;G</li><li class="repeat-mark">E&amp;G</li><li class="repeat-mark repeat-mark--hidden">E&amp;G</li><li class="repeat-mark repeat-mark--hidden">E&amp;G</li><li class="repeat-mark repeat-mark--hidden">E&amp;G</li><li class="repeat-mark">E&amp;G</li><li class="repeat-mark">E&amp;G</li>
        <li class="repeat-mark">E&amp;G</li><li class="repeat-mark">E&amp;G</li><li class="repeat-mark">E&amp;G</li><li class="repeat-mark">E&amp;G</li><li class="repeat-mark">E&amp;G</li><li class="repeat-mark">E&amp;G</li><li class="repeat-mark">E&amp;G</li>
        <li class="repeat-mark">E&amp;G</li><li class="repeat-mark">E&amp;G</li><li class="repeat-mark">E&amp;G</li><li class="repeat-mark">E&amp;G</li><li class="repeat-mark">E&amp;G</li><li class="repeat-mark">E&amp;G</li><li class="repeat-mark">E&amp;G</li>
        <li class="repeat-mark">E&amp;G</li><li class="repeat-mark">E&amp;G</li><li class="repeat-mark">E&amp;G</li><li class="repeat-mark">E&amp;G</li><li class="repeat-mark">E&amp;G</li><li class="repeat-mark">E&amp;G</li><li class="repeat-mark">E&amp;G</li>
      </ul>
      <div class="wedding-mark">
        <svg class="bracket" viewBox="0 0 12 92" aria-hidden="true">
          <path d="M11 1 H1 V91 H11" fill="none" stroke="var(--gold)" stroke-width="1.5"/>
        </svg>
        <h1 class="couple-names">
          <span class="first">Elena</span>
          <span class="second">&amp; Gavin</span>
        </h1>
        <svg class="bracket" viewBox="0 0 12 92" aria-hidden="true">
          <path d="M1 1 H11 V91 H1" fill="none" stroke="var(--gold)" stroke-width="1.5"/>
        </svg>
      </div>
    </section>
  </main>
</body>
</html>
```